Website Design for WeselneKarety.pl – Luxury Wedding Car Rental with Chauffeur

We are looking for a talented designer to create a modern, elegant, and fully responsive website for our new brand – WeselnyKarety.pl. We are a premium car rental platform in Poland, offering luxury and exotic vehicles exclusively for weddings. All cars come with a professional chauffeur, ensuring a high-end, stress-free, and stylish experience.
Website Purpose:
The website should present our offering in a luxurious, clear, and inspiring way. It must build trust, highlight the prestige of our brand, and encourage inquiries. Our target audience includes engaged couples, wedding planners, and clients seeking a truly exceptional vehicle for their special day.
Design Requirements:
Style: modern, elegant, minimalist
Color palette: white, black, gold, optionally silver – refined and luxurious
Typography: clean, modern, high-end
Layout: clear, intuitive, with large car images and well-defined sections
Fully responsive (desktop, tablet, mobile)
Bilingual layout (Polish/English) must be considered
Pages to Design:
Homepage
About Us
Fleet Overview
Individual Car Pages
Services (Weddings, Photo Shoots, Film Rentals)
Why Us / Unique Selling Points
Contact
FAQ
Inspiration:
Luxury automotive brands (e.g. Varnell-Dorne, Corwick, Elsby Havard)
High-end wedding websites
Minimalist layouts with large visuals and elegant typography
Additional Notes:
The design should evoke the emotions of a wedding day – elegance, uniqueness, style, and class. Please avoid flashy colors, excessive graphic effects, or overly decorative elements. Subtlety, prestige, and sophistication are key.

```html
<!DOCTYPE html>
<html lang="en">
<head>
<meta charset="utf-8">
<title>WeselneKarety – Luxury Wedding Cars</title>
<link href="https://fonts.googleapis.com/css2?family=Allura&family=Quicksand:wght@400;500;600&display=swap" rel="stylesheet">
<style>
:root{
  --navy:#142036;
  --navy-light:#1d2e48;
  --gold:#d8c36f;
  --gold-fill:#d6bf6b;
  --text:#d5dbe4;
  --muted:#aeb8c6;
  --line:#4a5870;
  --footer:#1b1b1c;
  --ink:#1a1d24;
}
*{margin:0;padding:0;box-sizing:border-box}
html,body{width:1200px;height:3315px;overflow:hidden}
body{background:var(--navy);color:var(--text);font-family:"Quicksand",sans-serif;position:relative}
.abs{position:absolute}
.script{font-family:"Allura",cursive;color:var(--gold);font-weight:400}
.brand{display:flex;align-items:center;gap:8px;color:var(--gold);font-size:20px;font-weight:600}
.brand i{width:14px;height:14px;border-radius:50%;background:var(--gold);display:block}
.nav{top:50px;display:flex;align-items:center;gap:8px;font-size:13px;letter-spacing:.5px;color:var(--text)}
.photo{position:absolute}
.btn-outline{position:absolute;height:45px;border:1px solid var(--line);color:var(--text);font-size:12px;letter-spacing:1px;display:flex;align-items:center;justify-content:center;gap:8px}
.btn-gold{position:absolute;height:40px;background:var(--gold-fill);color:var(--ink);font-size:12px;letter-spacing:1px;display:flex;align-items:center;justify-content:center}
.section-title{position:absolute;left:66px;font-size:24px;letter-spacing:3px;color:var(--text);font-weight:400}
.feature{position:absolute;top:1596px;width:348px;height:510px;border-left:1px solid var(--line)}
.feature .photo{left:0;top:0;width:100%;height:322px}
.feature h3{position:absolute;left:22px;top:346px;font-size:19px;letter-spacing:2px;font-weight:400}
.feature p{position:absolute;left:22px;top:384px;width:240px;font-size:15px;line-height:27px;letter-spacing:1px;color:var(--muted)}
.stat{position:absolute;top:2243px;width:256px;height:166px;border:1px solid var(--line);text-align:center;padding-top:68px}
.stat b{display:block;font-size:19px;letter-spacing:2px;font-weight:400}
.stat span{display:block;font-size:15px;letter-spacing:1px;color:var(--muted);margin-top:6px}
.footer{position:absolute;left:0;top:2925px;width:1200px;height:390px;background:var(--footer);color:#b9bcc2}
.footer h4{font-size:13px;font-weight:400;letter-spacing:.5px;color:#c8ccd2}
.footer ul{list-style:none;margin-top:16px}
.footer li{font-size:10px;line-height:25px}
.contact p{font-size:10px;line-height:16px}
.contact strong{font-weight:600}
.legal{position:absolute;top:3276px;font-size:10px}
</style>
</head>
<body>

<!-- Hero -->
<div class="photo" style="left:546px;top:0;width:654px;height:598px;background:linear-gradient(160deg,#8a6a45 0%,#5a4330 35%,#d9c6a8 55%,#3a2a22 80%,#1a1512 100%)" role="img" aria-label="Wedding car bonnet decorated with a cream rose and ribbon arrangement in front of an old stone building"></div>
<div class="abs brand" style="left:66px;top:44px"><i></i>WeselneKarety</div>
<div class="abs nav" style="left:927px">
  <svg width="14" height="14" viewBox="0 0 14 14" fill="none" stroke="#d5dbe4" stroke-width="1.3"><circle cx="6" cy="6" r="4.5"/><path d="M9.5 9.5L13 13"/></svg>FIND A CAR
</div>
<div class="abs nav" style="left:1068px">
  <svg width="16" height="12" viewBox="0 0 16 12" stroke="#d5dbe4" stroke-width="1.3"><path d="M1 1h14M1 6h10M1 11h14"/></svg>MENU
</div>
<h1 class="abs script" style="left:64px;top:228px;font-size:82px;white-space:nowrap;line-height:1">Dreams Arrive in Style</h1>
<p class="abs" style="left:66px;top:327px;width:400px;font-size:15px;line-height:27px;color:var(--text)">Elevate your wedding day with our curated collection of luxury vehicles, where every moment becomes an unforgettable memory.</p>
<div class="btn-outline" style="left:66px;top:432px;width:227px">RESERVE YOUR DREAM CAR
  <svg width="11" height="11" viewBox="0 0 11 11" stroke="#d5dbe4" stroke-width="1.2" fill="none"><path d="M1 10L10 1M3 1h7v7"/></svg></div>
<div class="btn-outline" style="left:310px;top:432px;width:206px">VIEW OUR COLLECTION
  <svg width="11" height="11" viewBox="0 0 11 11" stroke="#d5dbe4" stroke-width="1.2" fill="none"><path d="M1 10L10 1M3 1h7v7"/></svg></div>

<!-- Perfect match -->
<div class="abs" style="left:0;top:680px;width:1200px;display:flex;justify-content:center;align-items:baseline;gap:18px">
  <span style="font-size:22px;letter-spacing:2px">DISCOVER YOUR</span>
  <span class="script" style="font-size:50px">Perfect Match</span>
</div>
<div class="photo" style="left:153px;top:817px;width:245px;height:398px;background:linear-gradient(150deg,#5a3a32,#c9c0b4 55%,#8c7a70)" role="img" aria-label="Bride with bouquet inside a vintage car with a red steering wheel"></div>
<div class="photo" style="left:415px;top:782px;width:370px;height:468px;background:linear-gradient(180deg,#3a3d42,#1c1e22 60%,#2c2d30)" role="img" aria-label="Black luxury saloon parked on a city street"></div>
<div class="photo" style="left:802px;top:817px;width:245px;height:398px;background:linear-gradient(170deg,#c07a3a,#2a2e36 45%,#1a1c22 75%,#6a4a3a)" role="img" aria-label="Dark modern sedan decorated with white wedding flowers"></div>
<p class="abs" style="left:0;top:1294px;width:1200px;text-align:center;font-size:19px;line-height:32px;letter-spacing:1px">From classic Varnell-Dorne elegance to contemporary luxury,<br>find the vehicle that reflects your unique love story.</p>
<div class="btn-gold" style="left:504px;top:1376px;width:191px">VIEW OUR COLLECTION</div>

<!-- Excellence -->
<h2 class="section-title" style="top:1534px">WHERE ELEGANCE MEETS EXCELLENCE</h2>
<div class="feature" style="left:66px">
  <div class="photo" style="background:linear-gradient(160deg,#0d0d0f,#3a3b3e 50%,#8a8c90 62%,#2a0c0e)" role="img" aria-label="Silver luxury sedan in a dark studio"></div>
  <h3>UNPARALLELED LUXURY</h3><p>Handpicked premium vehicles maintained to perfection.</p>
</div>
<div class="feature" style="left:427px">
  <div class="photo" style="background:linear-gradient(170deg,#9a9c9e,#3a3c40 40%,#141517)" role="img" aria-label="Premium car interior with steering wheel and touchscreen"></div>
  <h3>WHITE-GLOVE SERVICE</h3><p>Professional chauffeurs and personalized wedding coordination.</p>
</div>
<div class="feature" style="left:787px">
  <div class="photo" style="background:linear-gradient(150deg,#b8bcc2,#2a3550 50%,#e6e4e0 75%,#3a3e48)" role="img" aria-label="Groom lifting bride beside a classic black car"></div>
  <h3>TIMELESS MEMORIES</h3><p style="width:270px">Creating picture-perfect moments for your special day.</p>
</div>

<!-- Trust -->
<h2 class="section-title" style="top:2182px">TRUSTED BY DISCERNING COUPLES</h2>
<div class="stat" style="left:66px"><b>500+</b><span>Magical Weddings</span></div>
<div class="stat" style="left:337px"><b>PREMIUM</b><span>Insurance Coverage</span></div>
<div class="stat" style="left:607px"><b>PROFESSIONAL</b><span>Chauffeur Team</span></div>
<div class="stat" style="left:877px"><b>5-STAR</b><span>Client Reviews</span></div>

<!-- CTA -->
<svg class="abs" style="left:0;top:2485px" width="1200" height="440" viewBox="0 0 1200 440">
  <rect width="1200" height="440" fill="#1b2b44"/>
  <path d="M0 120 Q600 -60 1200 120 L1200 0 L0 0Z" fill="#1f3049"/>
  <path d="M0 200 Q600 20 1200 200" fill="none" stroke="#26385a" stroke-width="30" opacity=".7"/>
  <path d="M0 440 Q600 360 1200 440Z" fill="#22344f"/>
</svg>
<h2 class="abs script" style="left:0;top:2570px;width:1200px;text-align:center;font-size:52px">Begin Your Journey</h2>
<p class="abs" style="left:0;top:2651px;width:1200px;text-align:center;font-size:18px;line-height:32px;letter-spacing:.5px">Let us help you create the entrance of your dreams.<br>Our wedding specialists are ready to bring your vision to life.</p>
<div class="btn-gold" style="left:502px;top:2758px;width:196px">START PLANNING TODAY</div>

<!-- Footer -->
<footer class="footer">
  <div class="abs brand" style="left:66px;top:47px"><i></i>WeselneKarety</div>
  <div class="abs" style="left:66px;top:102px">
    <h4>CREATING PERFECT BEGINNINGS</h4>
    <p style="font-size:10px;margin-top:2px">Wedding Transportation | Bridal Car Service | Luxury Chauffeur</p>
    <h4 style="margin-top:24px">FOLLOW US</h4>
    <p style="font-size:10px;margin-top:2px">Pictogram &nbsp; Friendbook &nbsp; Vidstream</p>
  </div>
  <div class="abs" style="left:455px;top:45px"><h4>EXPLORE</h4><ul>
    <li>Our Fleet</li><li>Wedding Services</li><li>Gallery</li><li>Testimonials</li><li>About Us</li><li>Pricing &amp; Packages</li><li>Wedding Planning Guide</li><li>FAQ</li></ul></div>
  <div class="abs" style="left:626px;top:45px"><h4>OUR OFFERINGS</h4><ul>
    <li>Classic Luxury Cars</li><li>Modern Premium Vehicles</li><li>Vintage Collection</li><li>Chauffeur Services</li><li>Wedding Coordination</li><li>Photography Support</li><li>Custom Packages</li><li>Event Transportation</li></ul></div>
  <div class="abs contact" style="left:867px;top:45px"><h4>GET IN TOUCH</h4>
    <div style="margin-top:18px"><p><strong>Contact Information:</strong></p><p>Phone: +1 (555) 010-2040</p><p>Email: bookings@velvetaislecars.com</p><p>Address: 48 Linden Row, Ashford Vale, CA 90311</p></div>
    <div style="margin-top:20px"><p><strong>Business Hours:</strong></p><p>Monday - Friday: 9:00 AM - 7:00 PM</p><p>Saturday: 10:00 AM - 4:00 PM</p><p>Sunday: By Appointment Only</p></div>
    <div style="margin-top:20px"><p><strong>Emergency Contact:</strong></p><p>24/7 Wedding Day Support: +1 (555) 010-7788</p></div>
  </div>
  <div class="abs" style="left:66px;top:335px;width:1067px;height:1px;background:#3a3c40"></div>
  <p class="abs" style="left:66px;top:351px;font-size:10px">Copyright © 2024 WeselnyKarety.pl. All Rights Reserved.</p>
  <p class="abs" style="left:758px;top:351px;font-size:10px;word-spacing:2px">Privacy Policy &nbsp;&nbsp; Terms of Service &nbsp;&nbsp; Cancellation Policy &nbsp;&nbsp; Insurance Information</p>
</footer>

</body>
</html>
```